Corbrook Estates LLC stationary for a real estate property management company.

Create stationary (letterhead, envelopes, business cards) using Corbrook Estates LLC logo as primary creative element. Stationary design needs to be horizontal, leaving as much space as possible for correspondence copy. See attached Creative Brief and past stationary files for details.

Target Market(s)

Prospective apartment residents and current residents, vendors, and government agencies.

Industry/Entity Type

Property Management

Contact Information for Business Card

Business card employee title: Property Manager. Should include address, phone, fax, email, website, slogan, and Corbrook Estates logo.

Font styles to use
Sans Serif

Colors
0592cd
000000

Requirements
Must have
• Tone should be conservative, institutional, business (i.e. banking, finance, real estate). Must include: address, phone, fax, website, and slogan (see attached Creative Brief). Should be a horizontal design, leaving as much room as possible for letter correspondence copy.
Nice to have
• Please use an Arial or Helvetica style font.
Should not have
• Letterhead layout should leave as much room as possible for copy.

```html
<!DOCTYPE html>
<html lang="en">
<head>
<meta charset="utf-8">
<title>Corbrook Estates LLC — Stationery</title>
<link href="https://fonts.googleapis.com/css2?family=Arimo:wght@400;700&family=Montserrat:wght@400;500;600;700&display=swap" rel="stylesheet">
<style>
  :root {
    --backdrop: #a1b2b1;
    --brand-blue: #1b74e4;
    --ink: #111111;
    --paper: #ffffff;
    --rule: #3a3a3a;
    --shadow: 6px 6px 7px rgba(0, 0, 0, 0.45);
  }
  * { box-sizing: border-box; margin: 0; padding: 0; }
  html, body { width: 1200px; height: 960px; overflow: hidden; }
  body {
    background: var(--backdrop);
    position: relative;
    font-family: "Arimo", Arial, sans-serif;
    color: var(--ink);
  }
  .sheet { position: absolute; box-shadow: var(--shadow); overflow: hidden; }

  /* Brand wordmark */
  .brand { display: flex; align-items: center; gap: 6px; }
  .brand-mark { flex: none; background: currentColor; }
  .brand-name {
    font-family: "Arimo", Arial, sans-serif;
    font-weight: 700;
    text-transform: uppercase;
    line-height: 1.05;
    letter-spacing: 0.02em;
    white-space: nowrap;
  }
  .brand--blue { color: var(--brand-blue); }
  .brand--black { color: var(--ink); }

  /* Business card front */
  .card-front { left: 26px; top: 102px; width: 262px; height: 156px; background: var(--brand-blue); }
  .card-front .brand { position: absolute; left: 52px; top: 56px; }
  .card-front .brand-mark { width: 30px; height: 30px; }
  .card-front .brand-name { font-size: 15px; }

  /* Business card back */
  .card-back { left: 26px; top: 285px; width: 262px; height: 156px; background: var(--paper); font-family: "Montserrat", Arial, sans-serif; }
  .card-back .brand { position: absolute; left: 9px; top: 19px; }
  .card-back .brand-mark { width: 20px; height: 20px; }
  .card-back .brand-name { font-size: 10px; }
  .card-back .divider { position: absolute; left: 131px; top: 18px; width: 1px; height: 120px; background: var(--rule); }
  .card-back .address { position: absolute; left: 9px; top: 68px; font-size: 8px; line-height: 10px; }
  .card-back .contacts { position: absolute; left: 9px; top: 100px; font-size: 8px; line-height: 10px; }
  .card-back .contacts .label { color: var(--brand-blue); display: inline-block; width: 30px; }
  .card-back .holder { position: absolute; left: 142px; top: 68px; }
  .holder-name { font-family: "Montserrat", Arial, sans-serif; font-weight: 600; font-size: 12.5px; white-space: nowrap; }
  .holder-title { font-family: "Montserrat", Arial, sans-serif; color: var(--brand-blue); font-size: 7px; letter-spacing: 0.06em; text-transform: uppercase; white-space: nowrap; }

  /* Letterhead */
  .letterhead { left: 311px; top: 75px; width: 419px; height: 586px; background: var(--paper); }
  .letterhead .brand { position: absolute; left: 8px; top: 21px; }
  .letterhead .brand-mark { width: 34px; height: 34px; }
  .letterhead .brand-name { font-size: 16px; }
  .letter-contact { position: absolute; left: 217px; top: 38px; display: flex; gap: 5px; font-family: "Montserrat", Arial, sans-serif; font-size: 6.6px; line-height: 9px; white-space: nowrap; }
  .letter-contact .col + .col { border-left: 1px solid var(--rule); padding-left: 5px; }
  .letter-contact strong { font-weight: 600; }
  .letter-contact .label { color: var(--brand-blue); }
  .letter-date { position: absolute; left: 20px; top: 102px; font-family: "Montserrat", Arial, sans-serif; font-size: 7.5px; }
  .letter-heading { position: absolute; left: 20px; top: 124px; font-family: "Montserrat", Arial, sans-serif; font-weight: 600; font-size: 8px; letter-spacing: 0.05em; }
  .letter-body { position: absolute; left: 20px; top: 144px; width: 380px; font-size: 6.9px; line-height: 9.7px; text-align: justify; }
  .letter-body p + p { margin-top: 9.7px; }
  .signature { position: absolute; left: 27px; top: 495px; width: 78px; height: 32px; background: linear-gradient(90deg, #ececec, #f7f7f7); }
  .letter-sign { position: absolute; left: 20px; top: 532px; }
  .letter-sign .holder-name { font-size: 12px; }
  .letter-sign .holder-title { font-size: 7px; }

  /* Presentation folder */
  .folder { left: 753px; top: 75px; width: 419px; height: 586px; background: var(--brand-blue); }
  .folder .brand { position: absolute; left: 191px; top: 503px; gap: 7px; }
  .folder .brand-mark { width: 48px; height: 48px; }
  .folder .brand-name { font-size: 22px; }

  /* Envelope front */
  .envelope-front { left: 322px; top: 684px; width: 399px; height: 206px; background: var(--paper); }
  .envelope-front .brand { position: absolute; left: 12px; top: 12px; gap: 5px; }
  .envelope-front .brand-mark { width: 26px; height: 26px; }
  .envelope-front .brand-name { font-size: 12.5px; }
  .envelope-front .return-address { position: absolute; left: 144px; top: 25px; border-left: 1px solid var(--rule); padding-left: 4px; font-family: "Montserrat", Arial, sans-serif; font-size: 6.6px; line-height: 9px; white-space: nowrap; }
  .return-address strong { font-weight: 600; }

  /* Envelope back */
  .envelope-back { left: 764px; top: 684px; width: 399px; height: 206px; background: var(--paper); }
  .envelope-back .flap { position: absolute; left: 0; top: 0; }
  .envelope-back .brand { position: absolute; left: 145px; top: 10px; gap: 5px; }
  .envelope-back .brand-mark { width: 22px; height: 22px; }
  .envelope-back .brand-name { font-size: 11px; }
</style>
</head>
<body>

<section class="sheet card-front" aria-label="Business card front">
  <div class="brand brand--black"><span class="brand-mark"></span><span class="brand-name">Corbrook<br>Estates LLC</span></div>
</section>

<section class="sheet card-back" aria-label="Business card back">
  <div class="brand brand--blue"><span class="brand-mark"></span><span class="brand-name">Corbrook<br>Estates LLC</span></div>
  <p class="address">2180 Alder Street #214<br>Fresno, CA93721</p>
  <p class="contacts">
    <span class="label">Phone</span>559-304-7715<br>
    <span class="label">Fax</span>559-304-7720<br>
    www.corbrookestates.us<br>
    daniel@corbrookestates.us
  </p>
  <div class="divider"></div>
  <div class="holder">
    <p class="holder-name">Daniel Hargrove</p>
    <p class="holder-title">Property Manager</p>
  </div>
</section>

<section class="sheet letterhead" aria-label="Letterhead">
  <div class="brand brand--blue"><span class="brand-mark"></span><span class="brand-name">Corbrook<br>Estates LLC</span></div>
  <div class="letter-contact">
    <div class="col"><strong>Estates LLC</strong><br>2180 Alder Street #214<br>Fresno, CA93721</div>
    <div class="col"><span class="label">Phone</span> 559-304-7715<br>www.corbrookestates.us<br>daniel@corbrookestates.us</div>
  </div>
  <p class="letter-date">Fresno, 25.06.2017</p>
  <p class="letter-heading">CORBROOK ESTATES LLC</p>
  <div class="letter-body">
    <p>Lorem ipsum dolor sit amet, consectetur adipiscing elit. Nunc blandit urna erat, id gravida est eleifend at. Fusce tristique mauris vel finibus fermentum. Curabitur vitae cursus lorem. Morbi non viverra sem, laoreet egestas orci. Lorem ipsum dolor sit amet, consectetur adipiscing elit. Phasellus egestas non mi non pellentesque. Mauris vitae felis nunc. Fusce ipsum tortor, malesuada sed dui quis, consectetur eleifend enim. Integer euismod mi ac suscipit congue. Integer interdum scelerisque ex. Nunc pellentesque elit non ante consectetur, sit amet pulvinar ante efficitur. Donec nisi massa, rutrum vitae lectus sit amet, eleifend dapibus sem. Phasellus at venenatis nunc. Nulla imperdiet lacus eros, id pellentesque nunc gravida a. Nulla non magna ut tellus feugiat blandit. Phasellus lobortis sed ipsum in scelerisque.</p>
    <p>Class aptent taciti sociosqu ad litora torquent per conubia nostra, per inceptos himenaeos. Nulla tristique metus quis felis bibendum feugiat. Curabitur placerat sollicitudin magna, ac molestie mi vulputate non. Integer sollicitudin odio vitae nibh egestas, et bibendum mi vehicula. Sed non orci dictum, facilisis erat a, tincidunt nibh. Quisque vulputate hendrerit quam, a fringilla odio egestas ut. Nulla bibendum id dolor ac sollicitudin. Maecenas eget lacus luctus, cursus augue quis, molestie neque. In consequat turpis in vulputate mollis. Class aptent taciti sociosqu ad litora torquent per conubia nostra, per inceptos himenaeos. Vestibulum a felis eu ante pellentesque tincidunt nec ut eros. Suspendisse dapibus dui sit amet mauris ultricies, ac maximus augue aliquam. Vestibulum non arcu sem. Vestibulum dignissim sodales sem, non mattis nisi faucibus sed.</p>
    <p>Nullam pretium dolor in diam rhoncus ornare. Donec et dictum elit, eu elementum sem. Aenean vitae sagittis eros. Sed vitae elit luctus, placerat arcu sed, imperdiet massa. Phasellus ac metus ullamcorper, blandit lorem sit amet, vulputate mauris. Praesent porta vel turpis quis lobortis. Fusce aliquet massa nibh, vitae cursus sapien laoreet at. Etiam eu blandit odio. Donec a tincidunt magna. Nulla facilisi.</p>
    <p>Donec posuere ipsum vitae ante tempor, eget fermentum orci fringilla. Praesent fringilla elementum elit, at semper turpis pulvinar nec. Quisque odio tellus, egestas id neque nec, rutrum finibus erat. Lorem ipsum dolor sit amet, consectetur adipiscing elit. Aenean leo nisl, consectetur vel posuere id, iaculis ac mauris. Maecenas vel sodales metus, vel rhoncus nunc. Pellentesque varius dui in nisl tempus, ac pharetra urna egestas. Donec maximus, sem at iaculis consectetur, massa nibh accumsan erat, a auctor lacus purus non erat. Aenean dapibus tincidunt suscipit. Etiam est enim, dignissim et arcu consectetur, vulputate lacinia felis. Sed nisi dui, maximus quis dui quis, ullamcorper sodales mauris. Donec vulputate libero sed finibus dictum. Aliquam massa orci, placerat vitae posuere sit amet, elementum nec tellus. Maecenas sollicitudin purus et urna sagittis ullamcorper. In et purus sit amet eros rutrum ullamcorper.</p>
    <p>Phasellus accumsan purus erat, ut laoreet risus viverra non. Morbi at lectus nec ante varius malesuada. Cras ex mauris, accumsan et eros ac, blandit dapibus dolor. Pellentesque turpis nisi, scelerisque nec feugiat dapibus, condimentum quis purus. Vestibulum blandit sapien in pellentesque rhoncus. Ut vel maximus lacus, ac porttitor nunc. Duis diam mi, rutrum et lobortis sit amet, rhoncus non lectus. Donec eros lectus, ornare a felis a, aliquam eleifend magna.</p>
  </div>
  <div class="signature" role="img" aria-label="Handwritten signature of the property manager"></div>
  <div class="letter-sign">
    <p class="holder-name">Daniel Hargrove</p>
    <p class="holder-title">Property Manager</p>
  </div>
</section>

<section class="sheet folder" aria-label="Presentation folder">
  <div class="brand brand--black"><span class="brand-mark"></span><span class="brand-name">Corbrook<br>Estates LLC</span></div>
</section>

<section class="sheet envelope-front" aria-label="Envelope front">
  <div class="brand brand--blue"><span class="brand-mark"></span><span class="brand-name">Corbrook<br>Estates LLC</span></div>
  <p class="return-address"><strong>Estates LLC</strong><br>2180 Alder Street #214<br>Fresno, CA93721</p>
</section>

<section class="sheet envelope-back" aria-label="Envelope back">
  <svg class="flap" width="399" height="54" viewBox="0 0 399 54" aria-hidden="true">
    <polygon points="0,0 399,0 371,54 28,54" fill="var(--brand-blue)"/>
  </svg>
  <div class="brand brand--black"><span class="brand-mark"></span><span class="brand-name">Corbrook<br>Estates LLC</span></div>
</section>

</body>
</html>
```